Biz Card for Harrowfield Property Partners - HWPP

Harrowfield Property Partners is a commercial real estate acquisitions firm. We buy commercial property and need to raise capital from investors for each deal we buy. The vibe needs to be: give us your money, we will multiply it.
Our website: www.hrwpp-example.com
Competitors are: https://velmarholdings-example.com/, https://tribanquepartners-example.com/, http://www.ostrellecapital-example.com/
Target Market(s)
High Net Worth Individuals, Bankers, Insurance Companies, Commercial Real Estate Brokers.
Industry/Entity Type
Investment Banking
Contact Information for Business Card
Name, Title, Addess, Cell#, Office#, email, website
Requirements
Must have
- use one of our logos. See website for look and feel: www.hrwpp-example.com
Nice to have
- see website: www.hrwpp-example.com

```html
<!DOCTYPE html>
<html lang="en">
<head>
<meta charset="utf-8">
<title>Harrowfield Property Partners – Business Card</title>
<link rel="stylesheet" href="https://fonts.googleapis.com/css2?family=Roboto:wght@400;500&display=swap">
<style>
  :root {
    --stage: #2c2c2e;
    --navy: #0b2640;
    --navy-deep: #0a1f36;
    --navy-light: #1f4a70;
    --white: #ffffff;
    --text-soft: #e6ecf2;
  }
  * { box-sizing: border-box; margin: 0; padding: 0; }
  html, body { width: 1200px; height: 800px; overflow: hidden; }
  body {
    background: var(--stage);
    font-family: "Roboto", Arial, sans-serif;
    display: flex;
    flex-direction: column;
    align-items: center;
    justify-content: center;
    gap: 40px;
  }
  .card {
    position: relative;
    width: 560px;
    height: 320px;
    overflow: hidden;
    box-shadow: 0 12px 30px rgba(0,0,0,.45);
  }

  /* Back side */
  .card-back { background: var(--navy); }
  .back-pattern {
    position: absolute; inset: 0;
    background: linear-gradient(110deg, var(--navy-deep) 0%, var(--navy) 55%, var(--navy-light) 100%);
  }
  .back-mark {
    position: absolute;
    left: 420px; top: 64px;
    width: 66px; height: 66px;
    border-radius: 50%;
    background: var(--white);
  }

  /* Front side */
  .card-front { background: var(--navy); }
  .front-shape { position: absolute; inset: 0; }
  .contact {
    position: absolute;
    left: 34px; top: 96px;
    color: var(--white);
  }
  .contact-name { font-size: 22px; font-weight: 500; line-height: 1.1; }
  .contact-title { font-size: 15px; color: var(--text-soft); margin-bottom: 14px; }
  .contact-list { list-style: none; }
  .contact-list li {
    display: flex; align-items: center; gap: 12px;
    font-size: 15px; line-height: 22px; color: var(--text-soft);
  }
  .contact-list svg { width: 13px; height: 13px; flex: none; }
  .contact-address {
    margin-top: 22px; margin-left: 25px;
    font-size: 15px; line-height: 20px; color: var(--text-soft);
  }
  .brand {
    position: absolute;
    left: 330px; top: 70px;
    width: 210px;
    text-align: center;
    color: var(--navy);
  }
  .brand-dot {
    width: 62px; height: 62px; border-radius: 50%;
    background: var(--navy);
    margin: 0 auto 14px;
  }
  .brand-name {
    font-size: 19px; font-weight: 400;
    letter-spacing: 3px; text-transform: uppercase; line-height: 1.35;
  }
</style>
</head>
<body>

  <section class="card card-back" aria-label="Card back">
    <div class="back-pattern" role="img" aria-label="Repeating pattern of circular emblems on navy"></div>
    <div class="back-mark"></div>
  </section>

  <section class="card card-front" aria-label="Card front">
    <svg class="front-shape" viewBox="0 0 560 320" aria-hidden="true">
      <path d="M262 40 A214 214 0 0 0 300 300" fill="none" stroke="#ffffff" stroke-width="4"/>
      <circle cx="470" cy="140" r="200" fill="#ffffff"/>
    </svg>

    <div class="contact">
      <p class="contact-name">Daniel Whitmore</p>
      <p class="contact-title">Manager</p>
      <ul class="contact-list">
        <li>
          <svg viewBox="0 0 24 24" fill="#fff"><path d="M6.6 10.8a15 15 0 0 0 6.6 6.6l2.2-2.2a1 1 0 0 1 1-.25 11 11 0 0 0 3.6.6 1 1 0 0 1 1 1V20a1 1 0 0 1-1 1A17 17 0 0 1 3 4a1 1 0 0 1 1-1h3.5a1 1 0 0 1 1 1c0 1.25.2 2.45.6 3.6a1 1 0 0 1-.25 1z"/></svg>
          (555) 214-0937
        </li>
        <li>
          <svg viewBox="0 0 24 24" fill="none" stroke="#fff" stroke-width="2"><rect x="3" y="5" width="18" height="14"/><path d="M3 6l9 7 9-7"/></svg>
          info@hrwpp-example.com
        </li>
        <li>
          <svg viewBox="0 0 24 24" fill="none" stroke="#fff" stroke-width="2"><circle cx="12" cy="12" r="9"/><path d="M3 12h18M12 3c3 3 3 15 0 18M12 3c-3 3-3 15 0 18"/></svg>
          www.hrwpp-example.com
        </li>
      </ul>
      <p class="contact-address">48 Linden Park Ave, Suite 910<br>Ashford Bay, FL 30021</p>
    </div>

    <div class="brand">
      <div class="brand-dot"></div>
      <p class="brand-name">Harrowfield Property Partners</p>
    </div>
  </section>

</body>
</html>
```